Customizable natural skin care line needs a product labels and logo design

We need product labels designed for plant based multitasking products with customizable options They are simple basic products that can be mixed at home,used in a way thats is beyond their intended function delivering a unique benefits Our Personalized and seasonal beauty offers versatility We are introducing 4 basic products ,6 additives with botanical extracts that help balance,nourish ,protect correct,energies and revive the skin and 2 seasonal products . Our products will help people address their own skin concerns and provide longer shelf life /Our products are safe for the environment and skin health and we like to see clean and simple Eco Labels Labels - that should communicate fresh,simple,fewer ingredients multi purpose. easy to mix

Target Market(s)

35 and up

Logo Text

Customize it ... blend ... mix .... Doesn’t have to have a text .. ?

Font styles to use
Serif

Colors

Designer to choose only greyscale colors for use in the design.

Requirements
Must have
• Most importantly is to know is that there are 2 different set of products that can be used as they are or enhanced with the other botanical additives ..customizable
for the products to give impression that they go together
The first set are the Basics ... second set treatment essence .. I open for new names
Nice to have
• Simple one color design easy to remember clean organic fresh

```html
<!DOCTYPE html>
<html lang="en">
<head>
<meta charset="utf-8">
<title>Blendleaf product labels</title>
<link href="https://fonts.googleapis.com/css2?family=Lora:wght@400;600&display=swap" rel="stylesheet">
<style>
  :root {
    --page: #ffffff;
    --ink: #111111;
    --rule-light: #9a9a9a;
    --frame: #bdbdbd;
    --tone: #6f6f6f;
    --tone-ink: #ffffff;
    --tone-rule: #cfcfcf;
  }
  * { margin: 0; padding: 0; box-sizing: border-box; }
  html, body { width: 848px; height: 1200px; overflow: hidden; background: var(--page); }
  body { position: relative; font-family: "Lora", Georgia, serif; }

  .label {
    position: absolute;
    width: 388px;
    height: 254px;
    color: var(--ink);
    --rule: var(--rule-light);
  }
  .label--light { left: 222px; top: 329px; background: #fff; border: 1px solid var(--frame); }
  .label--dark { left: 223px; top: 610px; background: var(--tone); color: var(--tone-ink); --rule: var(--tone-rule); }

  .divider { position: absolute; top: 18px; width: 1px; height: 220px; background: var(--rule); }
  .divider--left { left: 113px; }
  .divider--right { left: 274px; }

  .info { position: absolute; left: 9px; top: 14px; width: 98px; }
  .contact { font-size: 6.4px; line-height: 8.4px; font-weight: 600; }
  .origin { margin-top: 16px; font-size: 6.6px; font-weight: 600; }
  .ingredients-title { margin-top: 20px; font-size: 7.2px; font-weight: 600; }
  .ingredients { margin-top: 3px; font-size: 5.3px; line-height: 7.3px; text-align: justify; font-weight: 600; }
  .best-before { margin-top: 10px; font-size: 6px; font-weight: 600; }

  .brand {
    position: absolute; left: 113px; width: 161px; top: 66px;
    display: flex; flex-direction: column; align-items: center; gap: 12px;
  }
  .brand-dot { width: 58px; height: 58px; border-radius: 50%; background: currentColor; }
  .brand-name { font-size: 20px; letter-spacing: 3px; text-transform: lowercase; }

  .usage { position: absolute; left: 284px; top: 80px; width: 96px; }
  .usage-title { font-size: 7.2px; font-weight: 600; }
  .usage-text { margin-top: 3px; font-size: 5.3px; line-height: 6.9px; font-weight: 600; }
  .volume { position: absolute; left: 284px; top: 220px; font-size: 7.2px; font-weight: 600; }
</style>
</head>
<body>

<section class="label label--light">
  <div class="info">
    <p class="contact">companies name<br>street and house no<br>post code city, country<br>e-mail hello@blendleaf.org</p>
    <p class="origin">made in U.S.A</p>
    <p class="ingredients-title">INGREDIENTS/INCI</p>
    <p class="ingredients">aqua, sunflower seed oil, rosehip fruit oil, jojoba seed oil, calendula flower extract, almond seed oil, shea butter, aloe leaf juice, glycerin, squalane, rosemary leaf extract, chamomile flower extract, lavender oil, vitamin E, citric acid, xanthan gum, natural fragrance blend.</p>
    <p class="best-before">best used before</p>
  </div>
  <span class="divider divider--left"></span>
  <div class="brand">
    <span class="brand-dot"></span>
    <span class="brand-name">Blendleaf</span>
  </div>
  <span class="divider divider--right"></span>
  <div class="usage">
    <p class="usage-title">HOW IT WORKS</p>
    <p class="usage-text">we are aware that every skin is different and each skin type deserves its own care. That is why we give you simple basic products you can mix together, following a short recipe for your own routine.</p>
  </div>
  <p class="volume">50 ml/1.05 fl oz</p>
</section>

<section class="label label--dark">
  <div class="info">
    <p class="contact">companies name<br>street and house no<br>post code city, country<br>e-mail hello@blendleaf.org</p>
    <p class="origin">made in U.S.A</p>
    <p class="ingredients-title">INGREDIENTS/INCI</p>
    <p class="ingredients">aqua, sunflower seed oil, rosehip fruit oil, jojoba seed oil, calendula flower extract, almond seed oil, shea butter, aloe leaf juice, glycerin, squalane, rosemary leaf extract, chamomile flower extract, lavender oil, vitamin E, citric acid, xanthan gum, natural fragrance blend.</p>
    <p class="best-before">best used before</p>
  </div>
  <span class="divider divider--left"></span>
  <div class="brand">
    <span class="brand-dot"></span>
    <span class="brand-name">Blendleaf</span>
  </div>
  <span class="divider divider--right"></span>
  <div class="usage">
    <p class="usage-title">HOW IT WORKS</p>
    <p class="usage-text">we are aware that every skin is different and each skin type deserves its own care. That is why we give you simple basic products you can mix together, following a short recipe for your own routine.</p>
  </div>
  <p class="volume">50 ml/1.05 fl oz</p>
</section>

</body>
</html>
```